Massage-Creme label for a young pharmacy

We are a young pharmacy which is part of a big union. We developed for a customer a very good massage creme with aloe vera, coconut oil, and many more advantages and as well a massage jelly. All we need is a good and affordable label which is beatiful and helps us to promote our product. As we want to develop further products, it would be very cool to have a corporate label for all upcoming products.

Target Market(s)

professional masseurs and physiotherapists

Industry/Entity Type

Health And Wellness

Font styles to use
Sans Serif
Decorative

Colors

Designer to choose colors to be used in the design.

Requirements
Must have
• Professionally looking design (but I'm sure you are doing so... :-)
Nice to have
• Label can have any shape. What you see is just a bad label with corresponding sizes, so you can imagine how it would look like in the final state.
Should not have
• If possible, the label should not be completely black (although it might look cool) as we are printing it on our own Vostek qr318-ux and black is difficult to print (and very costy).

```html
<!DOCTYPE html>
<html lang="de">
<head>
<meta charset="utf-8">
<title>Massage-Crème Coconut – Aloe Vera Label</title>
<link href="https://fonts.googleapis.com/css2?family=Allura&family=Kalam:wght@700&family=Open+Sans:wght@600&display=swap" rel="stylesheet">
<style>
  :root {
    --page-bg: #ecebe8;
    --label-white: #ffffff;
    --ink: #1d1d1b;
    --leaf-green: #7dbb3c;
    --leaf-deep: #3f7f24;
    --leaf-light: #b8dc8f;
    --badge-red: #d3161f;
    --badge-ring: #e9e9e9;
    --arc-grey: #e6e7e6;
  }
  * { margin: 0; padding: 0; box-sizing: border-box; }
  html, body {
    width: 1200px;
    height: 1000px;
    overflow: hidden;
    background: var(--page-bg);
  }
  .label {
    position: absolute;
    left: 340px;
    top: 20px;
    width: 520px;
    height: 960px;
    background: var(--label-white);
    overflow: hidden;
  }
  .label__arc {
    position: absolute;
    left: 0;
    top: 40px;
    width: 520px;
    height: 200px;
  }
  .label__title {
    position: absolute;
    top: 138px;
    left: 0;
    width: 100%;
    text-align: center;
    white-space: nowrap;
    font-family: "Allura", cursive;
    font-weight: 400;
    font-size: 68px;
    line-height: 1;
    color: var(--ink);
  }
  .label__variant {
    position: absolute;
    top: 236px;
    left: 0;
    width: 100%;
    display: flex;
    align-items: center;
    justify-content: center;
    gap: 14px;
    white-space: nowrap;
    font-family: "Open Sans", sans-serif;
    font-weight: 600;
    font-size: 20px;
    letter-spacing: 0.3px;
    color: var(--leaf-green);
  }
  .label__variant::before,
  .label__variant::after {
    content: "";
    width: 52px;
    height: 2px;
    background: var(--leaf-green);
  }
  .label__visual {
    position: absolute;
    left: 0;
    top: 300px;
    width: 520px;
    height: 660px;
    background:
      linear-gradient(180deg, var(--label-white) 0%, rgba(255,255,255,0) 38%),
      linear-gradient(100deg, var(--leaf-light) 0%, var(--leaf-green) 45%, var(--leaf-deep) 100%);
  }
  .label__badge {
    position: absolute;
    left: 50px;
    top: 310px;
    width: 170px;
    height: 106px;
    transform: rotate(-12deg);
  }
  .label__badge-text {
    position: absolute;
    inset: 0;
    display: flex;
    flex-direction: column;
    align-items: center;
    justify-content: center;
    white-space: nowrap;
    font-family: "Kalam", cursive;
    font-weight: 700;
    font-size: 23px;
    line-height: 1.05;
    color: var(--label-white);
  }
</style>
</head>
<body>
  <main class="label">
    <svg class="label__arc" viewBox="0 0 520 200" aria-hidden="true">
      <path d="M20 200 Q260 -10 500 200" fill="none" stroke="var(--arc-grey)" stroke-width="3"/>
    </svg>

    <h1 class="label__title">Massage-Crème</h1>
    <p class="label__variant">COCONUT - ALOE VERA</p>

    <div class="label__visual" role="img" aria-label="Photo of aloe vera leaves with a small corked oil bottle and a halved coconut"></div>

    <div class="label__badge">
      <svg viewBox="0 0 170 106" width="170" height="106" aria-hidden="true">
        <ellipse cx="85" cy="53" rx="83" ry="51" fill="var(--badge-ring)"/>
        <ellipse cx="85" cy="53" rx="77" ry="45" fill="var(--badge-red)"/>
      </svg>
      <div class="label__badge-text"><span>Energetisch</span><span>leitend!</span></div>
    </div>
  </main>
</body>
</html>
```